Spy/Espionage/Counterintelligence Membership Community Needs a PowerPoint Template

We need a powerpoint template for one of our business verticals focused on spies, espionage, and counterintelligence. The name of it is "Pale Harbor Guild" and the logo is attached. Pale Harbor Guild is a community that connects people with experts in espionage and counterintelligence through an online social network, as well as in-person events. We would like to see designs that incorporate the red and black of the logo. The design should communicate mystery/suspense and peak curiosity.

Target Market(s)

Late 20s to baby boomers, male

Industry/Entity Type

Social Club

Font styles to use
Sans Serif

Colors
ec1f27
000000
ffffff

Requirements
Must have
• A user-friendly ppt template file. Incorporate basic fonts that don't have to be installed on every computer for presentations. A cover slide and a basic inside slide. A white background. I will also need graphic source files.
Nice to have
• Plenty of space for slide title and body content. Logo on every slide.
Should not have
• Inconsistency with fonts. Misalignment of images.

```html
<!DOCTYPE html>
<html lang="en">
<head>
<meta charset="utf-8">
<title>Pale Harbor Guild – Presentation Template</title>
<link rel="stylesheet" href="https://fonts.googleapis.com/css2?family=Open+Sans:ital,wght@0,300;0,400;0,600;1,400&family=Roboto+Condensed:wght@300;400;700&display=swap">
<style>
:root{
  --red:#ec1f27;
  --deep-red:#8c0d12;
  --black:#000;
  --white:#fff;
  --sheet:#d9d9d9;
  --grey:#9a9a9a;
  --mid-grey:#4a4a4a;
  --text:#555;
  --rule:#bdbdbd;
}
*{margin:0;padding:0;box-sizing:border-box}
html,body{width:1200px;height:914px;overflow:hidden;background:var(--sheet)}
body{font-family:"Open Sans",Arial,sans-serif;color:var(--text)}
.sheet{position:relative;width:1200px;height:914px;background:var(--sheet)}
.sheet::before{content:"";position:absolute;left:0;top:0;width:1200px;height:14px;background:#f2f2f2}
.slide{position:absolute;width:353px;height:272px;background:var(--white);overflow:hidden}
.c1{left:51px}.c2{left:409px}.c3{left:766px}
.r1{top:44px}.r2{top:321px}.r3{top:605px}
.abs{position:absolute}
.head{font-family:"Roboto Condensed",Arial,sans-serif;font-weight:700;text-transform:uppercase}

/* inner slide frame */
.band{position:absolute;left:0;top:0;width:353px;height:25px;background:var(--black)}
.band h2{position:absolute;left:14px;top:5px;font-family:"Roboto Condensed",Arial,sans-serif;font-weight:700;font-size:13px;color:var(--white);letter-spacing:.2px}
.band .accent{position:absolute;right:0;top:0;width:118px;height:25px;background:linear-gradient(90deg,var(--black),var(--deep-red) 30%,var(--red))}
.band-rule{position:absolute;left:0;top:26px;width:353px;height:1.5px;background:var(--red)}
.foot{position:absolute;left:14px;right:14px;top:256px;border-top:.6px solid var(--rule)}
.foot .mark{position:absolute;left:0;top:3px;display:flex;align-items:center;gap:3px;font-size:4px;font-weight:600;color:var(--black)}
.foot .mark i{display:block;width:8px;height:8px;border-radius:50%;background:var(--red)}
.foot .pg{position:absolute;right:0;top:3px;font-size:4.5px;color:#777}

.body{font-size:4.6px;line-height:7.4px;text-align:justify;color:var(--text)}
.body p+p{margin-top:7px}
.redcap{font-size:5.4px;line-height:7.6px;color:var(--red);text-transform:uppercase}
.photo{background:linear-gradient(120deg,#3a3a3a,#d4d4d4 45%,#8a8a8a)}

/* cover */
.cover-panel{left:6px;top:6px;width:341px;height:150px;background:radial-gradient(ellipse 140px 130px at 110px 70px,var(--deep-red),#2a0406 70%,var(--black))}
.cover-rule{left:6px;top:158px;width:341px;height:2px;background:var(--red)}
.cover-title{right:27px;top:66px;text-align:right;color:var(--white);font-size:15.5px;line-height:19px}
.cover-title .hl{color:var(--red)}
.cover-date{right:27px;top:107px;font-size:7px;color:var(--white)}
.logo-dot{border-radius:50%;background:var(--red)}
.logo-name{font-family:"Open Sans",Arial,sans-serif;font-weight:400;color:var(--black);white-space:nowrap}
.cover-base{left:0;top:266px;width:353px;height:6px;background:var(--black)}

/* about 3 */
.greyband{left:106px;top:64px;width:247px;height:66px;background:var(--mid-grey);padding:11px 14px 0 21px;font-style:italic;font-size:5.4px;line-height:12px;color:var(--white)}

/* chart legend */
.legend{left:217px;top:150px;width:86px;font-size:4.5px;color:#444}
.legend .row{display:flex;gap:4px;margin-bottom:7px}
.legend .sw{flex:none;width:5px;height:5px;margin-top:1px}
.legend small{display:block;font-size:3.4px;line-height:4.4px;color:#777;margin-top:2px}

/* rings */
.stat{position:absolute;top:84px;width:100px;text-align:center}
.stat .pct{font-family:"Roboto Condensed",Arial,sans-serif;font-weight:700;font-size:12px;color:var(--red);margin-top:3px}
.stat .body{text-align:center;font-size:4.3px;line-height:6.8px;color:#aaa;margin-top:2px}

/* team */
.lead{left:30px;top:62px;width:293px;text-align:center;font-style:italic;font-size:5px;line-height:10px;color:#333}
.member{position:absolute;top:94px;width:80px;text-align:center}
.member .face{width:52px;height:52px;margin:0 auto;border-radius:50%;border:1.5px solid var(--red);background:linear-gradient(160deg,#e8e8e8,#8f8f8f)}
.member h3{font-size:6px;font-weight:400;color:var(--red);margin-top:10px}
.member .role{font-size:4.3px;font-style:italic;color:#555;margin-top:1px}
.member .body{font-size:4.3px;line-height:9.6px;color:#aaa;margin-top:6px}

/* image slide */
.dark-half{left:0;top:0;width:180px;height:272px;background:var(--black);color:var(--white)}
.dark-half .body{color:#eee;font-size:4.4px;line-height:7.2px}
.brand-mini{left:7px;top:249px;display:flex;align-items:center;gap:4px;font-size:6px;font-weight:600;color:var(--white);letter-spacing:.4px}
.brand-mini i{display:block;width:9px;height:9px;background:#bbb}

/* section slide */
.section{background:radial-gradient(ellipse 150px 150px at 140px 90px,#5a0508,#220103 65%,var(--black))}
.section h2{left:202px;top:166px;font-family:"Roboto Condensed",Arial,sans-serif;font-weight:300;font-size:15px;color:var(--red)}
.section .body{color:#ddd}

/* contact slide */
.map{left:0;top:83px;width:353px;height:103px;background:linear-gradient(135deg,#e7ecd9,#cfe0ee 40%,#eef0e6 70%,#dfe6d2)}
.contact{left:0;top:186px;width:353px;height:86px;background:var(--black);color:#ddd;font-size:5.3px;line-height:6.4px}
.contact .item{position:absolute;display:flex;gap:5px;align-items:flex-start}
.contact svg{flex:none}
.contact-rule{left:0;top:269px;width:353px;height:3px;background:var(--red)}
.social{display:flex;gap:3px}
.social i{display:block;width:8px;height:8px;background:var(--red)}
</style>
</head>
<body>
<main class="sheet">

  <!-- Cover -->
  <section class="slide c1 r1">
    <div class="abs cover-panel" role="img" aria-label="Dark red and black brand graphic fading into the background"></div>
    <div class="abs head cover-title">Welcome<br><span class="hl">To</span> Our Presentation</div>
    <div class="abs cover-date">Birmingham, March 25, 2011</div>
    <div class="abs cover-rule"></div>
    <div class="abs logo-dot" style="left:247px;top:182px;width:46px;height:46px"></div>
    <div class="abs logo-name" style="left:0;width:353px;text-align:center;padding-left:186px;padding-right:0;top:232px;font-size:16px;letter-spacing:-.4px;left:-86px">Pale Harbor Guild</div>
    <div class="abs cover-base"></div>
  </section>

  <!-- About us: team photo -->
  <section class="slide c2 r1">
    <header class="band"><h2>ABOUT US</h2><div class="accent"></div></header>
    <div class="band-rule"></div>
    <div class="abs photo" style="left:14px;top:50px;width:323px;height:74px" role="img" aria-label="Black and white photo of a business team standing in a row"></div>
    <div class="abs redcap" style="left:14px;top:144px;width:110px">Lorem ipsum dolor sit met consectur adipiscing elit, sed do euismod tempor incididunt ut labore et delore magna</div>
    <div class="abs body" style="left:132px;top:144px;width:203px">
      <p>Lorem ipsum dolor sit amet, consectetur adipiscing elit, sed do eiusmod tempor incididunt ut labore et dolore magna aliqua. Ut enim ad minim veniam, quis nostrud exercitation ullamco laboris nisi ut aliquip ex ea commodo consequat. Duis aute irure dolor in reprehenderit in voluptate velit esse cillum dolore eu fugiat nulla pariatur.</p>
      <p>Lorem ipsum dolor sit amet, consectetur adipiscing elit, sed do eiusmod tempor incididunt ut labore et dolore magna aliqua. Ut enim ad minim veniam, quis nostrud exercitation ullamco laboris nisi ut aliquip ex ea commodo consequat. Duis aute irure dolor in reprehenderit in voluptate velit esse cillum dolore eu.</p>
    </div>
    <footer class="foot"><div class="mark"><i></i>Pale Harbor Guild</div><div class="pg">2</div></footer>
  </section>

  <!-- About us: feature -->
  <section class="slide c3 r1">
    <header class="band"><h2>ABOUT US</h2><div class="accent"></div></header>
    <div class="band-rule"></div>
    <div class="abs" style="left:0;top:64px;width:106px;height:66px;background:var(--mid-grey)"></div>
    <div class="abs photo" style="left:13px;top:60px;width:93px;height:72px" role="img" aria-label="Black and white portrait of a businesswoman"></div>
    <div class="abs greyband">Lorem ipsum dolor sit amet<br>consectetur adipiscing elit, sed do eiusmod tempor incididunt ut<br>labore et dolore magna aliqua. Ut enim ad minim veniam, quis</div>
    <div class="abs body" style="left:128px;top:140px;width:192px;font-size:4.2px;line-height:6.9px">
      <p>Lorem ipsum dolor sit amet, consectetur adipiscing elit, sed do eiusmod tempor incididunt ut labore et dolore magna aliqua. Ut enim ad minim veniam, quis nostrud exercitation ullamco laboris nisi ut aliquip ex ea commodo consequat. Duis aute irure dolor in reprehenderit in voluptate velit esse cillum dolore eu fugiat nulla pariatur.</p>
      <p>Lorem ipsum dolor sit amet, consectetur adipiscing elit, sed do eiusmod tempor incididunt ut labore et dolore magna aliqua. Ut enim ad minim veniam, quis nostrud exercitation ullamco laboris nisi ut aliquip ex ea commodo consequat. Duis aute irure dolor in reprehenderit in voluptate velit esse cillum dolore eu.</p>
      <p>Fugiat nulla pariatur. Excepteur sint occaecat cupidatat non proident, sunt in culpa qui officia deserunt mollit anim id est laborum. Excepteur sint occaecat cupidatat non proident, sunt in consequat. Duis aute irure dolor in reprehenderit in voluptate velit esse cillum dolore eu.</p>
    </div>
    <footer class="foot"><div class="mark"><i></i>Pale Harbor Guild</div><div class="pg">2</div></footer>
  </section>

  <!-- About us: chart -->
  <section class="slide c1 r2">
    <header class="band"><h2>ABOUT US</h2><div class="accent"></div></header>
    <div class="band-rule"></div>
    <div class="abs body" style="left:26px;top:54px;width:144px;font-size:4.5px;line-height:9.3px">
      <p><span style="color:var(--red)">Lorem ipsum dolor sit amet</span><br>consectetur adipiscing elit, sed do eiusmod tempor incididunt ut labore et dolore magna aliqua. Ut enim ad minim veniam, quis nostrud exercitation ullamco laboris nisi ut aliquip ex ea commodo consequat. Duis aute irure dolor in reprehenderit in voluptate velit esse cillum dolore eu fugiat nulla pariatur.</p>
      <p><span style="color:var(--red)">Lorem ipsum dolor sit amet</span><br>consectetur adipiscing elit, sed do eiusmod tempor incididunt ut labore et dolore magna aliqua. Ut enim ad minim veniam, quis nostrud exercitation ullamco laboris nisi ut aliquip ex ea commodo consequat. Duis aute irure dolor in reprehenderit in voluptate velit esse cillum dolore eu</p>
      <p><span style="color:var(--red)">Lorem ipsum dolor sit amet</span><br>Excepteur sint occaecat cupidatat non proident, sunt in culpa qui officia deserunt mollit anim id est laborum. Excepteur sint occaecat cupidatat non</p>
    </div>
    <svg class="abs" style="left:190px;top:44px" width="145" height="100" viewBox="0 0 145 100" aria-label="Bar chart 2009 to 2012">
      <line x1="3" y1="0" x2="3" y2="84" stroke="#bbb" stroke-width=".6"/>
      <line x1="3" y1="84" x2="140" y2="84" stroke="#bbb" stroke-width=".6"/>
      <g>
        <rect x="10" y="28" width="8" height="56" fill="#ec1f27"/><rect x="19" y="52" width="8" height="32" fill="#9a9a9a"/><rect x="28" y="58" width="8" height="26" fill="#000"/>
        <rect x="44" y="48" width="8" height="36" fill="#ec1f27"/><rect x="53" y="29" width="8" height="55" fill="#9a9a9a"/><rect x="62" y="52" width="8" height="32" fill="#000"/>
        <rect x="78" y="36" width="8" height="48" fill="#ec1f27"/><rect x="87" y="60" width="8" height="24" fill="#9a9a9a"/><rect x="96" y="45" width="8" height="39" fill="#000"/>
        <rect x="112" y="35" width="8" height="49" fill="#ec1f27"/><rect x="121" y="53" width="8" height="31" fill="#9a9a9a"/><rect x="130" y="30" width="8" height="54" fill="#000"/>
        <rect x="51" y="10" width="10" height="6" fill="#bbb"/><text x="56" y="14.3" font-size="3.4" fill="#fff" text-anchor="middle" font-family="Open Sans, sans-serif">72%</text>
        <rect x="77" y="19" width="10" height="6" fill="#ec1f27"/><text x="82" y="23.3" font-size="3.4" fill="#fff" text-anchor="middle" font-family="Open Sans, sans-serif">64%</text>
        <rect x="129" y="13" width="10" height="6" fill="#222"/><text x="134" y="17.3" font-size="3.4" fill="#fff" text-anchor="middle" font-family="Open Sans, sans-serif">61%</text>
      </g>
      <g font-size="5.5" fill="#444" text-anchor="middle" font-family="Open Sans, sans-serif">
        <text x="23" y="95">2009</text><text x="57" y="95">2010</text><text x="91" y="95">2011</text><text x="125" y="95">2012</text>
      </g>
    </svg>
    <div class="abs legend">
      <div class="row"><span class="sw" style="background:var(--red)"></span><div>LOREM IPSUM<small>Lorem ipsum dolor sit amet, consectetur adipiscing elit, sed do eiusmod tempor incididunt ut labore et dolore magna</small></div></div>
      <div class="row"><span class="sw" style="background:var(--grey)"></span><div>LOREM IPSUM<small>Lorem ipsum dolor sit amet, consectetur adipiscing elit, sed do eiusmod tempor incididunt ut labore et dolore magna</small></div></div>
      <div class="row"><span class="sw" style="background:var(--black)"></span><div>LOREM IPSUM</div></div>
    </div>
    <footer class="foot"><div class="mark"><i></i>Pale Harbor Guild</div><div class="pg">2</div></footer>
  </section>

  <!-- About us: stats -->
  <section class="slide c2 r2">
    <header class="band"><h2>ABOUT US</h2><div class="accent"></div></header>
    <div class="band-rule"></div>

    <div class="stat" style="left:13px">
      <svg width="58" height="58" viewBox="0 0 58 58" aria-label="81 percent">
        <circle cx="29" cy="29" r="25" fill="none" stroke="#9a9a9a" stroke-width="5"/>
        <circle cx="29" cy="29" r="25" fill="none" stroke="#ec1f27" stroke-width="5" stroke-dasharray="50 107" transform="rotate(-90 29 29)"/>
        <circle cx="29" cy="29" r="25" fill="none" stroke="#333" stroke-width="5" stroke-dasharray="38 119" transform="rotate(110 29 29)"/>
        <circle cx="29" cy="29" r="7" fill="none" stroke="#777" stroke-width="4" stroke-dasharray="2.5 1.5"/>
        <circle cx="29" cy="29" r="3" fill="#777"/>
      </svg>
      <div class="pct">81%</div>
      <div class="body">dolor sit amet, consectetur adipiscing elit, sed do eiusmod tempor incididunt ut labore et dolore magna aliqua. Ut enim ad minim veniam, quis nostrud exercitation ullamco laboris nisi ut aliquip ex ea cesse cillum dolore eu fugiat nulla pariatur.</div>
    </div>
    <div class="stat" style="left:131px">
      <svg width="58" height="58" viewBox="0 0 58 58" aria-label="72 percent">
        <circle cx="29" cy="29" r="25" fill="none" stroke="#9a9a9a" stroke-width="5"/>
        <circle cx="29" cy="29" r="25" fill="none" stroke="#ec1f27" stroke-width="5" stroke-dasharray="70 87" transform="rotate(-90 29 29)"/>
        <circle cx="29" cy="29" r="25" fill="none" stroke="#333" stroke-width="5" stroke-dasharray="40 117" transform="rotate(160 29 29)"/>
        <rect x="21" y="30" width="4" height="7" fill="#777"/><rect x="27" y="26" width="4" height="11" fill="#777"/><rect x="33" y="28" width="4" height="9" fill="#777"/>
        <path d="M21 26 L29 20 L33 22" fill="none" stroke="#777" stroke-width="1.6"/>
      </svg>
      <div class="pct">72%</div>
      <div class="body">dolor sit amet, consectetur adipiscing elit, sed do eiusmod tempor incididunt ut labore et dolore magna aliqua. Ut enim ad minim veniam, quis nostrud exercitation ullamco laboris nisi ut aliquip ex ea cesse cillum dolore eu fugiat nulla pariatur.</div>
    </div>
    <div class="stat" style="left:241px">
      <svg width="58" height="58" viewBox="0 0 58 58" aria-label="63 percent">
        <circle cx="29" cy="29" r="25" fill="none" stroke="#9a9a9a" stroke-width="5"/>
        <circle cx="29" cy="29" r="25" fill="none" stroke="#ec1f27" stroke-width="5" stroke-dasharray="30 127" transform="rotate(120 29 29)"/>
        <circle cx="29" cy="29" r="25" fill="none" stroke="#333" stroke-width="5" stroke-dasharray="50 107" transform="rotate(170 29 29)"/>
        <rect x="21" y="23" width="16" height="11" fill="none" stroke="#777" stroke-width="1.6"/><rect x="26" y="35" width="6" height="2" fill="#777"/>
      </svg>
      <div class="pct">63%</div>
      <div class="body">dolor sit amet, consectetur adipiscing elit, sed do eiusmod tempor incididunt ut labore et dolore magna aliqua. Ut enim ad minim veniam, quis nostrud exercitation ullamco laboris nisi ut aliquip ex ea cesse cillum dolore eu fugiat nulla pariatur.</div>
    </div>
    <footer class="foot"><div class="mark"><i></i>Pale Harbor Guild</div><div class="pg">2</div></footer>
  </section>

  <!-- About us: team -->
  <section class="slide c3 r2">
    <header class="band"><h2>ABOUT US</h2><div class="accent"></div></header>
    <div class="band-rule"></div>
    <p class="abs lead">dolor sit amet, consectetur adipiscing elit, sed do eiusmod tempor incididunt ut labore et dolore magna aliqua.<br>Ut enim ad minim veniam, quis nostrud exercitation ullamco laboris nisi ut a</p>
    <div class="member" style="left:32px">
      <div class="face" role="img" aria-label="Portrait photo of Jonathan Doe"></div>
      <h3>JONATHAN DOE</h3><div class="role">President</div>
      <div class="body" style="text-align:justify">dolor sit amet, consectetur adipiscing elit, sed do eiusmod tempor incididunt ut labore et dolore magna aliqua. Ut enim ad minim veniam, quis nostrud exercitation</div>
    </div>
    <div class="member" style="left:141px">
      <div class="face" role="img" aria-label="Portrait photo of Melanie Doe"></div>
      <h3>MELANIE DOE</h3><div class="role">CEO / Founder</div>
      <div class="body" style="text-align:justify">dolor sit amet, consectetur adipiscing elit, sed do eiusmod tempor incididunt ut labore et dolore magna aliqua. Ut enim ad minim veniam, quis nostrud exercitation</div>
    </div>
    <div class="member" style="left:246px">
      <div class="face" role="img" aria-label="Portrait photo of Natalie Doe"></div>
      <h3>NATALIE DOE</h3><div class="role">Vice President</div>
      <div class="body" style="text-align:justify">dolor sit amet, consectetur adipiscing elit, sed do eiusmod tempor incididunt ut labore et dolore magna aliqua. Ut enim ad minim veniam, quis nostrud exercitation</div>
    </div>
    <footer class="foot"><div class="mark"><i></i>Pale Harbor Guild</div><div class="pg">2</div></footer>
  </section>

  <!-- Image text -->
  <section class="slide c1 r3" style="left:53px">
    <div class="abs dark-half">
      <h2 class="abs head" style="left:14px;top:15px;font-size:13px">IMAGE TEXT</h2>
      <div class="abs" style="left:29px;top:100px;font-size:5.3px">LOREM IPSUM DOLOR SIT MET</div>
      <div class="abs body" style="left:29px;top:113px;width:131px">
        <p>Lorem ipsum dolor sit amet, consectetur adipiscing elit, sed do eiusmod tempor incididunt ut labore et dolore magna aliqua. Ut enim ad minim veniam, quis nostrud exercitation ullamco laboris nisi ut aliquip ex ea commodo consequat. Duis aute irure dolor in reprehenderit in voluptate velit esse cillum dolore eu fugiat nulla pariatur.</p>
        <p>Lorem ipsum dolor sit amet, consectetur adipiscing elit, sed do eiusmod tempor incididunt ut labore et dolore magna aliqua. Ut enim ad minim veniam, quis nostrud exercitation ullamco laboris nisi ut aliquip ex ea commodo consequat. Duis aute irure dolor in reprehenderit in voluptate velit esse cillum dolore eu</p>
      </div>
      <div class="abs brand-mini"><i></i>NORTHLINE</div>
    </div>
    <div class="abs photo" style="left:180px;top:0;width:173px;height:272px;background:linear-gradient(160deg,#f4f4f4,#bdbdbd 50%,#5a5a5a)" role="img" aria-label="Black and white photo of a smiling woman and man"></div>
  </section>

  <!-- Section title -->
  <section class="slide c2 r3 section" style="left:411px" role="img" aria-label="Dark red brand graphic on black">
    <h2 class="abs head">SECTION TITLE</h2>
    <div class="abs body" style="left:202px;top:186px;width:130px">Lorem ipsum dolor sit amet, consectetur adipiscing elit, sed do eiusmod tempor incididunt ut labore et dolore magna aliqua. Ut enim ad minim veniam, quis nostrud exercitation ullamco laboris nisi ut aliquip ex ea commodo consequat. Duis aute irure dolor in reprehenderit in</div>
  </section>

  <!-- Contact -->
  <section class="slide c3 r3" style="left:767px">
    <div class="abs logo-dot" style="left:45px;top:18px;width:37px;height:37px"></div>
    <div class="abs logo-name" style="left:14px;top:60px;font-size:15px;letter-spacing:-.4px">Pale Harbor Guild</div>
    <div class="abs map" role="img" aria-label="Street map showing the office location"></div>
    <div class="abs contact">
      <div class="item" style="left:28px;top:26px">
        <svg width="8" height="8" viewBox="0 0 10 10"><path d="M5 1 L9 5 H8 V9 H6 V6 H4 V9 H2 V5 H1 Z" fill="#ec1f27"/></svg>
        <span>4120 Alder Quay Ste 300<br>Westmoor, Oregon 97001</span>
      </div>
      <div class="item" style="left:28px;top:46px">
        <svg width="8" height="8" viewBox="0 0 10 10"><path d="M2 1 L4 1 L5 3.5 L3.8 4.5 Q4.8 6.3 5.6 6.2 L6.5 5 L9 6 L9 8 Q6 10 3 6.5 Q1 4 2 1 Z" fill="#ec1f27"/></svg>
        <span>1.800.555.0142</span>
      </div>
      <div class="item" style="left:28px;top:64px">
        <svg width="8" height="8" viewBox="0 0 10 10"><path d="M2 1 L4 1 L5 3.5 L3.8 4.5 Q4.8 6.3 5.6 6.2 L6.5 5 L9 6 L9 8 Q6 10 3 6.5 Q1 4 2 1 Z" fill="#ec1f27"/></svg>
        <span>503.555.0187</span>
      </div>
      <div class="item" style="left:133px;top:26px">
        <svg width="8" height="8" viewBox="0 0 10 10"><rect x="1" y="2" width="8" height="6" fill="none" stroke="#ec1f27" stroke-width="1.3"/><path d="M1 2 L5 5.5 L9 2" fill="none" stroke="#ec1f27" stroke-width="1.1"/></svg>
        <span>hello@paleharborguild.org</span>
      </div>
      <div class="item" style="left:133px;top:45px">
        <svg width="8" height="8" viewBox="0 0 10 10"><circle cx="5" cy="5" r="4" fill="none" stroke="#ec1f27" stroke-width="1.2"/><path d="M1 5 H9 M5 1 Q2.5 5 5 9 Q7.5 5 5 1" fill="none" stroke="#ec1f27" stroke-width=".8"/></svg>
        <span>www.paleharborguild.org</span>
      </div>
      <div class="item social" style="left:133px;top:63px"><i></i><i></i><i></i></div>
    </div>
    <div class="abs contact-rule"></div>
  </section>

</main>
</body>
</html>
```